We are looking to improve our packaging, because we are wanting to secure our products into five star hotels, spa and wellness centres and maybe even high end retail department stores. That is why it is important it must look the part. We are even prepared to change our current packaging (White stand up pouches) for something different e.g box etc...

Please keep in mind when designing our new Serenova packaging that our product range will extend to Room Sprays, Candles, Diffuser, Essential Oils, Soaps, Body Scrubs, Milk Baths, Body Lotions, Face Products. So the design will need to compliment and we must be able to adjust the artwork with ease to fit bottles big and small, tubes, boxes glass jars etc... at later stage.

Please see inspiration images of packaging I like. But please do not copy them. We would like something that is unique to our brand that will last for 2-4 years before we have to change the packaging again.

Our current packaging is in a white stand up pouches.
Updates

Project Deadline Extended Reason: Hi All,I have decided to extend the Serenova Calm Mix Packaging project as the designs I have received are not what I am looking for and are not polished enough for the retail health and spa market. Some of the ideas I received are on the right track, but they need to be reworked a bit more to give our packaging a premium high end looking product. I am trying to get our products into large retail outlets department stores, Chemists, Health and natural product stores, 5 star spa resorts and hotels and eventually export it globally and with so many similar products available for sale our products needs to stand out from the rest of the competition. We use premium grade salts with natural and organic ingredients in our products when we make them. They do not have any harsh chemicals in them. At the moment I am keeping to the stand up white pouches for now, but this will change later this year to a box. We have a good product that sells well, but our current look and feel of our packaging is letting us down and making it difficult to market into the bigger retail stores. I have attached a few sample ideas of what we like, but with our own unique mark to it. We would like something that is unique to us to give our Serenova brand its own identity. I will leave this up to your creative skills.Our Serenova product range will branch out to the following in a couple of months. Body Scrubs, Liquid Soaps, Soaps, Body and Face Lotions, Milk baths, Bath and Spa Tea Bags, Bubble Paths, Herbal and Fragranced Bath & Spa products, Steam Therapy, Massage and Bath Oils, Room Sprays, Home Fragrances and Essential oils. So please keep this mind when designing a label that it must be easily adapted to different shapes and size products. e.g. boxes, jars, tubes and bottles.If you have any question before you start, please send me a message.Thank you for taking the time to read our extended brief and very excited to see your designs. Kind Regards, Added Saturday, January 9, 2016

Target Market(s)

Male and female, natural products, well-being, holistic, wellness centres, spa resorts, 5 stars hotels and upmarket.

Industry/Entity Type

Health And Wellness

Font styles to use
Serif
Sans Serif
Other font styles liked:
• Open Sans

Requirements
Must have
• Front: Company Name: Brand name Serenova Calm Mix (See logo attached or feel fry to add your design flair to this). Please insert Front Packaging copy, 100% pure & natural logo, weight of item 1kg
• Back: Talvex logo (attached), Australian Packed & Owned logo (attached or you can just use type), Please use Back Packaging copy attached. Please allow space for barcode, Batch number and expiry date.
Nice to have
• Vector background, natural earthy feel, natural or organic textures
• but we are open to any suggestions you might have.

```html
<!DOCTYPE html>
<html lang="en">
<head>
<meta charset="utf-8">
<title>Serenova Calm Mix – Bath Soak Label</title>
<link rel="stylesheet" href="https://fonts.googleapis.com/css2?family=Lobster&family=Cinzel:wght@400&family=Crimson+Text:wght@400&display=swap">
<style>
  :root {
    --stage: #0f2a15;
    --paper: #ffffff;
    --teal: #7cc8aa;
    --orange: #d8782f;
    --gold: #c9a035;
    --leaf: #7fb24a;
    --mint: #4fe0b8;
    --ink: #555555;
    --frame: #6a6a6a;
    --seal-green: #2fa57a;
    --seal-dark: #4a4a4a;
  }
  * { box-sizing: border-box; margin: 0; padding: 0; }
  html, body { width: 1200px; height: 886px; overflow: hidden; }
  body {
    background: radial-gradient(ellipse at center, #123d1c 0%, var(--stage) 70%, #07150a 100%);
    position: relative;
  }
  .label {
    position: absolute;
    left: 303px; top: 23px;
    width: 593px; height: 840px;
    background: var(--paper);
    overflow: hidden;
  }
  .pattern {
    position: absolute;
    opacity: 0.55;
  }
  .pattern--top {
    left: 0; top: 0; width: 410px; height: 620px;
    background: linear-gradient(to bottom, var(--orange) 0%, #e08a2a 35%, var(--gold) 65%, var(--leaf) 100%);
    -webkit-mask-image: radial-gradient(ellipse 100% 100% at 0% 0%, #000 45%, transparent 100%);
    mask-image: radial-gradient(ellipse 100% 100% at 0% 0%, #000 45%, transparent 100%);
  }
  .pattern--bottom {
    left: 0; top: 560px; width: 593px; height: 280px;
    background: linear-gradient(to right, var(--leaf) 0%, #5fd0a0 45%, var(--mint) 100%);
    -webkit-mask-image: linear-gradient(to bottom, transparent 0%, #000 35%);
    mask-image: linear-gradient(to bottom, transparent 0%, #000 35%);
  }
  .art { position: absolute; left: 0; top: 0; width: 593px; height: 840px; }
  .title {
    position: absolute; left: 71px; width: 450px;
    text-align: center;
    font-family: "Lobster", cursive;
    color: var(--teal);
    line-height: 1;
  }
  .title--brand { top: 322px; font-size: 82px; }
  .title--line { top: 402px; left: 110px; font-size: 48px; }
  .product {
    position: absolute; left: 71px; width: 450px; top: 456px;
    text-align: center;
    font-family: "Cinzel", serif;
    font-size: 38px; color: var(--ink);
    line-height: 1;
  }
  .blurb {
    position: absolute; left: 100px; width: 392px; top: 512px;
    text-align: center;
    font-family: "Crimson Text", serif;
    font-size: 12.6px; line-height: 17px; color: var(--ink);
  }
  .ingredients {
    position: absolute; left: 0; top: 733px; width: 593px; height: 41px;
    background: var(--orange);
    display: flex; align-items: center; gap: 14px;
    padding-left: 26px;
    font-family: "Crimson Text", serif;
    font-size: 16.5px; letter-spacing: -0.4px; color: #fff;
    text-transform: uppercase;
  }
  .ingredient { display: flex; align-items: center; gap: 6px; white-space: nowrap; }
  .plus {
    width: 18px; height: 18px; border-radius: 50%;
    background: #6e6e6e; position: relative; flex: none;
  }
  .plus::before, .plus::after {
    content: ""; position: absolute; background: #fff;
    left: 50%; top: 50%; transform: translate(-50%, -50%);
  }
  .plus::before { width: 10px; height: 3px; }
  .plus::after { width: 3px; height: 10px; }
  .weight {
    position: absolute; right: 34px; top: 797px;
    font-family: "Crimson Text", serif;
    font-size: 17px; color: var(--ink);
  }
</style>
</head>
<body>
  <main class="label">
    <div class="pattern pattern--top" role="img" aria-label="Ornate paisley and floral pattern in orange and gold"></div>
    <div class="pattern pattern--bottom" role="img" aria-label="Ornate paisley and floral pattern in green and mint"></div>

    <svg class="art" viewBox="0 0 593 840" aria-hidden="true">
      <!-- satisfaction seal -->
      <g class="seal">
        <polygon points="445,190 420,262 438,255 448,275 470,205" fill="#239066"/>
        <polygon points="517,190 542,262 524,255 514,275 492,205" fill="#239066"/>
        <circle cx="481" cy="137" r="76" fill="var(--seal-green)"/>
        <circle cx="481" cy="137" r="58" fill="var(--seal-dark)"/>
        <circle cx="481" cy="137" r="37" fill="#f1f1f1"/>
      </g>
      <!-- name frame with arch -->
      <path d="M71.5,281 H216 V252 A80,53 0 0 1 376,252 V281 H521.5 V577 H71.5 Z"
            fill="#fff" stroke="var(--frame)" stroke-width="3"/>
      <path d="M77.5,287 H222 V252 A74,47 0 0 1 370,252 V287 H515.5 V571 H77.5 Z"
            fill="none" stroke="var(--frame)" stroke-width="1"/>
      <!-- origin badge -->
      <g class="origin-badge">
        <circle cx="296" cy="282" r="56" fill="#8a8a8a"/>
        <circle cx="296" cy="282" r="48" fill="#5c5c5c"/>
        <circle cx="296" cy="282" r="30" fill="#c9c9c9"/>
      </g>
    </svg>

    <h1 class="title title--brand">Serenova</h1>
    <h2 class="title title--line">Calm Mix</h2>
    <p class="product">BATH SOAK</p>
    <p class="blurb">A unique blend of himalayan and magnesium flakes for the ultimate therapeutic bath soak. Our Serenova Calm Mix will detoxify and revitalise your body.</p>

    <ul class="ingredients">
      <li class="ingredient"><span class="plus"></span>Himalayan Salt</li>
      <li class="ingredient"><span class="plus"></span>Magnesium Chloride Flakes</li>
      <li class="ingredient"><span class="plus"></span>Vitamin C</li>
    </ul>

    <p class="weight">1KG</p>
  </main>
</body>
</html>
```